Maple Vital App Landing Page

Looking for a landing page for our app at maplevitalco.com

Target Market(s)

Health care facilities

Industry/Entity Type

Healthcare

Number of Pages Required

1 page

```html
<!DOCTYPE html>
<html lang="en">
<head>
<meta charset="utf-8">
<title>Maple Vital App Landing Page</title>
<link rel="stylesheet" href="https://fonts.googleapis.com/css2?family=Open+Sans:wght@400;600&family=Roboto:wght@400;500&family=Poppins:wght@400&display=swap">
<style>
  :root {
    --page-bg: #d9e5f0;
    --brand-blue: #0a80f2;
    --label-blue: #1f72b8;
    --title-ink: #2f3336;
    --white: #ffffff;
    --ink: #222222;
    --soft-blue: #4fa3f7;
    --pale-blue: #cfe4fb;
  }
  * { box-sizing: border-box; margin: 0; padding: 0; }
  html, body { width: 848px; height: 1200px; overflow: hidden; }
  body {
    background: var(--page-bg);
    position: relative;
    font-family: "Roboto", Arial, sans-serif;
  }
  .page-title {
    position: absolute; top: 17px; left: 0; width: 848px;
    text-align: center;
    font-family: "Open Sans", Arial, sans-serif;
    font-weight: 600; font-size: 33px; letter-spacing: 0.3px;
    color: var(--title-ink);
  }
  .screen-label {
    position: absolute; width: 264px; text-align: center;
    font-family: "Open Sans", Arial, sans-serif;
    font-size: 27px; color: var(--label-blue);
  }
  .screen {
    position: absolute; width: 264px; height: 470px; overflow: hidden;
  }
  .col-left { left: 117px; }
  .col-right { left: 449px; }
  .row-top { top: 130px; }
  .row-bottom { top: 687px; }
  .label-top { top: 84px; }
  .label-bottom { top: 640px; }

  .brand {
    position: absolute; left: 0; width: 264px; text-align: center;
  }
  .brand-name {
    display: inline-flex; align-items: center; gap: 7px;
    font-family: "Roboto", Arial, sans-serif; font-weight: 500;
    font-size: 25px; color: var(--brand-blue); letter-spacing: -0.3px;
  }
  .brand-dot {
    width: 14px; height: 14px; border-radius: 50%;
    background: var(--brand-blue); display: inline-block;
  }
  .brand-tagline {
    margin-top: 4px;
    font-family: "Poppins", Arial, sans-serif;
    font-size: 11px; color: var(--brand-blue);
  }

  .splash { background: var(--white); }
  .splash .brand { top: 320px; }

  .walkthrough { background: var(--brand-blue); color: var(--white); text-align: center; }
  .walkthrough .art {
    position: absolute; left: 44px; top: 58px; width: 176px; height: 185px;
    border-radius: 48% 52% 40% 45%;
    background: linear-gradient(160deg, var(--soft-blue), #f2b035 85%);
  }
  .walkthrough .headline {
    position: absolute; top: 262px; width: 100%;
    font-size: 16px; font-weight: 500; line-height: 20px;
  }
  .walkthrough .body-copy {
    position: absolute; top: 319px; left: 26px; width: 212px;
    font-size: 9.4px; line-height: 11.3px;
  }
  .walkthrough .next-link {
    position: absolute; top: 424px; left: 222px; font-size: 11px;
  }

  .app-header {
    position: absolute; top: 0; left: 0; width: 264px; height: 73px;
    background: var(--brand-blue); color: var(--white); text-align: center;
  }
  .app-header .header-title {
    position: absolute; top: 20px; width: 100%;
    font-size: 16.5px; font-weight: 500; letter-spacing: 0.2px;
  }
  .app-header .header-sub {
    position: absolute; top: 46px; width: 100%; font-size: 12px;
  }
  .back-chevron { position: absolute; left: 12px; top: 23px; }

  .landing { background: var(--white); }
  .landing .app-header { border-radius: 0 0 8px 8px; }
  .landing .brand { top: 106px; }
  .landing .art {
    position: absolute; left: 20px; top: 168px; width: 222px; height: 196px;
    background: linear-gradient(90deg, var(--brand-blue) 0 18%, #f4f6f9 18% 80%, var(--brand-blue) 80%);
    border-radius: 40px;
  }

  .primary-button {
    position: absolute; left: 29px; width: 206px; height: 31px;
    background: var(--brand-blue); color: var(--white);
    font-size: 11px; text-align: center; line-height: 31px; border-radius: 2px;
  }
  .landing .primary-button, .screening .primary-button { top: 415px; }

  .screening { background: var(--white); }
  .screening .role-panel {
    position: absolute; top: 0; left: 0; width: 264px; height: 318px;
    background: var(--brand-blue); border-radius: 0 0 8px 8px;
  }
  .screening .app-header { border-bottom: 1px solid rgba(255,255,255,0.8); }
  .role-question {
    position: absolute; top: 80px; width: 100%; text-align: center;
    color: var(--white); font-size: 15px;
  }
  .role-card {
    position: absolute; width: 96px; height: 88px;
    background: var(--white); border-radius: 8px;
    text-align: center; color: var(--brand-blue);
    font-size: 12px; font-weight: 500;
  }
  .role-card .role-icon {
    position: absolute; left: 33px; top: 12px; width: 30px; height: 34px;
    border-radius: 6px; background: var(--pale-blue);
  }
  .role-card .role-name { position: absolute; bottom: 10px; width: 100%; }
  .role-card.is-selected {
    background: var(--brand-blue); color: var(--white);
    border: 1.5px solid var(--white);
  }
  .role-card.is-selected .role-icon { background: rgba(255,255,255,0.35); left: 31.5px; top: 10.5px; }
  .role-card.is-selected .role-name { bottom: 8.5px; }
  .facility-question {
    position: absolute; top: 329px; width: 100%; text-align: center;
    color: var(--brand-blue); font-size: 15px;
  }
  .facility-select {
    position: absolute; top: 354px; left: 29px; width: 206px; height: 30px;
    border: 1px solid var(--brand-blue); border-radius: 3px;
    padding-left: 8px; line-height: 28px; font-size: 11px; color: var(--ink);
  }
</style>
</head>
<body>
  <h1 class="page-title">MAPLE VITAL APP LANDING PAGE</h1>

  <h2 class="screen-label col-left label-top">Splash Screen</h2>
  <section class="screen splash col-left row-top">
    <div class="brand">
      <div class="brand-name"><span class="brand-dot"></span>MAPLE VITAL</div>
      <div class="brand-tagline">Keeping you safe.</div>
    </div>
  </section>

  <h2 class="screen-label col-right label-top">Walkthrough Screen</h2>
  <section class="screen walkthrough col-right row-top">
    <div class="art" role="img" aria-label="Illustration of a seated person wearing a face mask"></div>
    <p class="headline">Find What You<br>Need Service COVID -19</p>
    <p class="body-copy">COVID-19 symptoms can range from very mild to severe. Some people have no symptoms, People who are older or have existing chronic medical conditions.</p>
    <span class="next-link">Next</span>
  </section>

  <h2 class="screen-label col-left label-bottom">Landing Screen</h2>
  <section class="screen landing col-left row-bottom">
    <header class="app-header">
      <div class="header-title">COVID -19 SCREENING</div>
      <div class="header-sub">WELCOME</div>
    </header>
    <div class="brand">
      <div class="brand-name"><span class="brand-dot"></span>MAPLE VITAL</div>
      <div class="brand-tagline">Keeping you safe.</div>
    </div>
    <div class="art" role="img" aria-label="Illustration of three masked people walking outdoors"></div>
    <div class="primary-button">Start COVID-19 Screening</div>
  </section>

  <h2 class="screen-label col-right label-bottom">Screening - 1 Screen</h2>
  <section class="screen screening col-right row-bottom">
    <div class="role-panel"></div>
    <header class="app-header">
      <svg class="back-chevron" width="10" height="16" viewBox="0 0 10 16" aria-hidden="true">
        <polyline points="8,1 2,8 8,15" fill="none" stroke="#ffffff" stroke-width="1.4"/>
      </svg>
      <div class="header-title">COVID -19 SCREENING</div>
      <div class="header-sub">STEP - 1</div>
    </header>
    <div class="role-question">Who are you?</div>
    <div class="role-card" style="left:27px; top:105px;">
      <div class="role-icon" role="img" aria-label="Staff member icon"></div>
      <div class="role-name">STAFF</div>
    </div>
    <div class="role-card" style="left:139px; top:105px;">
      <div class="role-icon" role="img" aria-label="Healthcare provider icon"></div>
      <div class="role-name">PROVIDER</div>
    </div>
    <div class="role-card is-selected" style="left:27px; top:205px;">
      <div class="role-icon" role="img" aria-label="Visitor check-in icon"></div>
      <div class="role-name">VISITOR</div>
    </div>
    <div class="role-card" style="left:139px; top:205px;">
      <div class="role-icon" role="img" aria-label="Vendor icon"></div>
      <div class="role-name">VENDOR</div>
    </div>
    <div class="facility-question">Which facility are you at?</div>
    <div class="facility-select">Please pick one</div>
    <div class="primary-button">Next</div>
  </section>
</body>
</html>
```